Buch-/E-Book-Cover
Zielgruppe
Wir verkaufen Trainings und vermitteln über unser Buch ein erstes vertieftes Wissen zum Thema Vermögensaufbau.
Aufgabenstellung
Es soll schlicht und schön sein, Angelehnt an Tall coin short coin, bzw. an Schau hin und bleib Klug von Bartholo Fenwick.
Wir benötigen die AI, etc Dateien und die fertigen Dateien für Velmora.de Lumora sowie Velmora.de Books (ehemals Printvale) mit fertigem Cover.
Vorgaben von Velmora.de über die Homepage. Anbei ein Beispiel (wegen Velmora.de Buchnummer etc) Abstände, Buchrücken etc.
Buch ca. 150 Seiten
https://www.velmora-beispiel.de/Gaertner-bleiben-heute-Zeichen-guten/dp/7392058164 Front und Backcover kann man sich da ansehen.
Der Buchtitel ist 'Baue Kredite und bleib frei' - - Lassen Sie uns freundschaftlich in entspannter Atmosphäre über Immobilien sprechen (der nebentitel so klein wie bei Tall Coin - Short Coin)
Rücktitel: Bitte zuerst Platzhalter.
Ich bitte um 5x8 inch, also wie DIN A 5, wir nehmen cremefarbenes Papier denke ich. Die Seitenzahl kann ich auf die Seite noch nicht sagen, wir haben aber 75 Din A4 Seiten, sprich nach Formatierung eher 160-165 Din A5. WErde ich Ihnen final nach dem Gewinn sagen.
Versuchen Sie mich mal aus dem einen Bild raus zu schneiden, und dass dann mit einem Layer über das cover zu legen.
2-3 Versionen wäre gut, mit 2-3 Bildern. Buchrücken ein kleines Bild von mir.
Seite vom Buch: Titel nochmal.

```html
<!DOCTYPE html>
<html lang="de">
<head>
<meta charset="utf-8">
<title>Baue Kredite und bleib frei – Cover-Varianten</title>
<link rel="stylesheet" href="https://fonts.googleapis.com/css2?family=Lato:wght@300;400;900&display=swap">
<style>
  :root {
    --page-bg: #ffffff;
    --navy-deep: #0b1422;
    --navy: #1b2a40;
    --gold: #d2bc86;
    --white: #ffffff;
    --wine-dark: #1a0b0c;
    --wine: #4a1417;
    --suit-brown: #4a3a30;
    --suit-dark: #2e231d;
    --shirt-blue: #c9dcef;
  }
  * { box-sizing: border-box; margin: 0; padding: 0; }
  html, body {
    width: 1200px;
    height: 3000px;
    overflow: hidden;
    background: var(--page-bg);
    font-family: "Lato", Arial, sans-serif;
  }
  .canvas {
    position: relative;
    width: 1200px;
    height: 3000px;
  }
  .cover {
    position: absolute;
    overflow: hidden;
    color: var(--white);
  }
  .cover--navy {
    left: 258px; top: 240px;
    width: 752px; height: 1168px;
    background: radial-gradient(ellipse at 55% 45%, var(--navy) 0%, var(--navy-deep) 75%);
  }
  .cover--wine {
    left: 266px; top: 1590px;
    width: 736px; height: 1170px;
    background: linear-gradient(180deg, var(--wine) 0%, var(--wine-dark) 100%);
  }
  .portrait {
    position: absolute;
  }
  .cover--navy .portrait {
    left: 252px; top: 16px;
    width: 446px; height: 1152px;
    border-radius: 120px 120px 0 0;
    background: linear-gradient(180deg, #6b5040 0%, var(--suit-brown) 22%, var(--shirt-blue) 40%, var(--suit-brown) 55%, var(--suit-dark) 100%);
  }
  .cover--wine .portrait {
    left: 150px; top: 40px;
    width: 586px; height: 1130px;
    border-radius: 200px 200px 0 0;
    background: linear-gradient(180deg, #3a2a22 0%, #8a6650 28%, var(--suit-brown) 45%, var(--suit-dark) 100%);
  }
  .author {
    position: absolute;
    font-size: 22px;
    line-height: 27px;
    font-weight: 400;
    letter-spacing: 0.2px;
  }
  .cover--navy .author { left: 64px; top: 50px; }
  .cover--wine .author { left: 62px; top: 46px; }
  .title {
    position: absolute;
    font-size: 106px;
    line-height: 100px;
    letter-spacing: -2px;
  }
  .title__strong {
    display: block;
    font-weight: 900;
    color: var(--gold);
  }
  .title__light {
    display: block;
    font-weight: 300;
    color: var(--white);
  }
  .cover--navy .title { left: 64px; top: 590px; }
  .cover--wine .title { left: 62px; top: 536px; }
  .subtitle {
    position: absolute;
    font-size: 26px;
    line-height: 31px;
    font-weight: 400;
  }
  .cover--navy .subtitle { left: 68px; top: 1040px; width: 660px; }
  .cover--wine .subtitle { left: 66px; top: 968px; width: 460px; }
</style>
</head>
<body>
<main class="canvas">

  <section class="cover cover--navy" role="img" aria-label="Dunkelblauer Hintergrund mit goldenen Zierlinien">
    <div class="portrait" role="img" aria-label="Freigestelltes Foto des Autors im braunen Anzug, stehend, Hände in den Taschen"></div>
    <p class="author">CORVIN MADDOX –<br>Der WohnwertBerater</p>
    <h1 class="title">
      <span class="title__strong">BAUE</span>
      <span class="title__strong">KREDITE</span>
      <span class="title__light">UND BLEIB</span>
      <span class="title__light">FREI</span>
    </h1>
    <p class="subtitle">Lassen Sie uns unter Freunden in entspannter<br>Atmosphäre über Immobilien sprechen</p>
  </section>

  <section class="cover cover--wine" role="img" aria-label="Hintergrund mit dunkelrotem Streifenmuster">
    <div class="portrait" role="img" aria-label="Freigestelltes Porträtfoto des Autors im braunen Anzug mit verschränkten Armen"></div>
    <p class="author">CORVIN MADDOX –<br>Der WohnwertBerater</p>
    <h1 class="title">
      <span class="title__strong">BAUE</span>
      <span class="title__strong">KREDITE</span>
      <span class="title__light">UND BLEIB</span>
      <span class="title__light">FREI</span>
    </h1>
    <p class="subtitle">Lassen Sie uns unter Freunden<br>in entspannter Atmosphäre<br>über Immobilien sprechen</p>
  </section>

</main>
</body>
</html>
```